A Maple Syrup Label for a Local Buniness

We are looking for a label for our maple syrup business. Our business currently sells honey, and we are expanding into maple syrup. Our Business name is "Corvale Bees" and we currently have a logo attached below. We would like to incorporate the bee and CB part, but the label could also read "Corvale Farms" with the words maple syrup. We do not want consumers to confuse the maple syrup jars with the honey jars. It should be clear that the jars contain maple syrup. We are open to new designs as well.

```html
<!DOCTYPE html>
<html lang="en">
<head>
<meta charset="utf-8">
<title>Corvale Farms Maple Syrup Label</title>
<link href="https://fonts.googleapis.com/css2?family=Lobster&family=Merriweather:wght@400&family=Michroma&family=Roboto+Condensed:wght@400;700&display=swap" rel="stylesheet">
<style>
  :root {
    --maple-brown: #9a5410;
    --label-black: #050505;
    --label-white: #ffffff;
    --maple-gold: #f5b90a;
  }
  * { box-sizing: border-box; margin: 0; padding: 0; }
  html, body { width: 766px; height: 1200px; overflow: hidden; }
  body {
    background: var(--maple-brown);
    position: relative;
    font-family: "Roboto Condensed", sans-serif;
    color: var(--label-white);
    -webkit-font-smoothing: antialiased;
  }
  .label {
    position: absolute;
    top: 384px;
    width: 343px;
    height: 432px;
  }
  .label--front { left: 35px; }
  .label--back { left: 390px; }
  .label-shape { position: absolute; inset: 0; }
  .maple-leaf {
    position: absolute;
    left: 149px;
    width: 44px;
    height: 46px;
    background: var(--maple-gold);
    border-radius: 50% 50% 40% 40%;
  }
  .maple-leaf--top { top: 40px; }
  .maple-leaf--bottom { top: 350px; }

  .brand {
    position: absolute;
    top: 98px;
    left: 0;
    width: 343px;
    text-align: center;
  }
  .brand-dot {
    display: block;
    width: 16px;
    height: 16px;
    border-radius: 50%;
    background: var(--maple-gold);
    margin: 0 auto 6px;
  }
  .brand-name {
    font-family: "Merriweather", serif;
    font-size: 15px;
    line-height: 19px;
    color: var(--label-white);
    letter-spacing: 0.5px;
  }
  .certified {
    position: absolute;
    top: 176px;
    left: 0;
    width: 343px;
    text-align: center;
    font-family: "Michroma", sans-serif;
    font-size: 8.5px;
    letter-spacing: 2px;
    line-height: 12px;
    color: var(--label-white);
  }
  .certified .pure { letter-spacing: 5px; display: block; }

  .title-block {
    position: absolute;
    top: 206px;
    left: 40px;
    width: 264px;
    height: 126px;
  }
  .title-swoosh { position: absolute; inset: 0; }
  .title-script {
    position: absolute;
    top: 18px;
    left: 0;
    width: 264px;
    text-align: center;
    font-family: "Lobster", cursive;
    font-size: 50px;
    line-height: 56px;
    color: var(--label-white);
    transform: rotate(-12deg);
    white-space: nowrap;
  }
  .volume {
    position: absolute;
    top: 330px;
    left: 0;
    width: 343px;
    text-align: center;
    font-size: 10px;
    color: var(--label-white);
  }

  .nutrition {
    position: absolute;
    top: 88px;
    left: 86px;
    width: 170px;
    height: 208px;
    border: 1px solid var(--label-white);
    border-radius: 10px;
    padding: 6px;
    color: var(--label-white);
  }
  .nutrition-table {
    border: 2px solid var(--label-white);
    border-radius: 4px;
    height: 100%;
    display: flex;
    flex-direction: column;
    font-size: 8px;
    line-height: 11.5px;
    font-weight: 400;
    color: var(--label-white);
  }
  .nutrition-title {
    font-weight: 700;
    font-size: 13.5px;
    line-height: 17px;
    text-align: center;
    border-bottom: 2px solid var(--label-white);
    color: var(--label-white);
  }
  .serving-size {
    font-weight: 700;
    padding: 1px 3px;
    border-bottom: 2px solid var(--label-white);
    color: var(--label-white);
  }
  .servings { border-bottom: 2px solid var(--label-white); padding: 1px 3px; }
  .servings li { list-style: none; position: relative; color: var(--label-white); }
  .checkbox {
    position: absolute;
    right: 24px;
    top: 3px;
    width: 6px;
    height: 6px;
    border: 1px solid var(--label-white);
    border-radius: 1px;
  }
  .nutrient-grid { display: grid; grid-template-columns: 56px 1fr 1fr; flex: 1; }
  .nutrient-grid > div {
    border-left: 1.5px solid var(--label-white);
    text-align: center;
    padding: 2px 0;
    color: var(--label-white);
  }
  .nutrient-grid > div:nth-child(3n+1) {
    border-left: none;
    text-align: left;
    padding-left: 3px;
  }
  .nutrient-grid .head {
    border-bottom: 1.5px solid var(--label-white);
    height: 32px;
    font-size: 7px;
    line-height: 10px;
    padding-top: 5px;
  }
  .nutrient-grid .values { padding-top: 4px; }

  .back-footer {
    position: absolute;
    top: 304px;
    left: 94px;
    width: 164px;
    height: 44px;
    display: flex;
    align-items: center;
    gap: 6px;
    color: var(--label-white);
  }
  .mini-brand {
    font-family: "Merriweather", serif;
    font-size: 5.5px;
    line-height: 7px;
    text-align: center;
    width: 34px;
  }
  .mini-brand .brand-dot { width: 6px; height: 6px; margin-bottom: 2px; }
  .mini-title {
    width: 62px;
    text-align: center;
    font-family: "Michroma", sans-serif;
    font-size: 3.5px;
    letter-spacing: 0.6px;
    line-height: 5px;
  }
  .mini-script {
    margin-top: 2px;
    font-family: "Lobster", cursive;
    font-size: 12px;
    line-height: 14px;
    letter-spacing: 0;
    transform: rotate(-10deg);
    white-space: nowrap;
  }
  .contact {
    display: flex;
    gap: 3px;
    align-items: center;
    font-size: 3.5px;
    line-height: 4.5px;
    width: 50px;
  }
  .contact-icon {
    flex: none;
    width: 7px;
    height: 7px;
    border-radius: 50%;
    border: 1.5px solid var(--label-white);
  }
</style>
</head>
<body>

<section class="label label--front">
  <svg class="label-shape" viewBox="0 0 343 432" aria-hidden="true">
    <ellipse cx="171.5" cy="216" rx="169" ry="213" fill="var(--label-black)" stroke="var(--label-white)" stroke-width="5"/>
    <ellipse cx="171.5" cy="216" rx="155" ry="199" fill="none" stroke="var(--maple-gold)" stroke-width="5" stroke-linecap="round" stroke-dasharray="0 9"/>
  </svg>
  <div class="maple-leaf maple-leaf--top" role="img" aria-label="Gold maple leaf ornament"></div>
  <div class="brand">
    <span class="brand-dot"></span>
    <p class="brand-name">CORVALE<br>FARMS</p>
  </div>
  <p class="certified">CERTIFIED ORGANIC<span class="pure">PURE</span></p>
  <div class="title-block">
    <svg class="title-swoosh" viewBox="0 0 264 126" aria-hidden="true">
      <path d="M8 104 C 70 84, 170 70, 256 60 L 258 72 C 176 84, 80 100, 14 122 Z" fill="var(--label-white)" stroke="var(--maple-gold)" stroke-width="3" stroke-linejoin="round"/>
    </svg>
    <h1 class="title-script">Maple Syrup</h1>
  </div>
  <p class="volume">12.7 FLOZ. (375m)</p>
  <div class="maple-leaf maple-leaf--bottom" role="img" aria-label="Gold maple leaf ornament"></div>
</section>

<section class="label label--back">
  <svg class="label-shape" viewBox="0 0 343 432" aria-hidden="true">
    <ellipse cx="171.5" cy="216" rx="169" ry="213" fill="var(--label-black)" stroke="var(--label-white)" stroke-width="5"/>
    <ellipse cx="171.5" cy="216" rx="155" ry="199" fill="none" stroke="var(--maple-gold)" stroke-width="5" stroke-linecap="round" stroke-dasharray="0 9"/>
  </svg>
  <div class="maple-leaf maple-leaf--top" role="img" aria-label="Gold maple leaf ornament"></div>

  <div class="nutrition">
    <div class="nutrition-table">
      <h2 class="nutrition-title">Nutrition Information</h2>
      <p class="serving-size">Serving Size: 20g (1 Tablespoon)</p>
      <ul class="servings">
        <li>- Servings per 250g jar: 12.5<span class="checkbox"></span></li>
        <li>- Servings per 500g jar: 25.0<span class="checkbox"></span></li>
        <li>- Servings per 1kg jar: 50.0<span class="checkbox"></span></li>
      </ul>
      <div class="nutrient-grid">
        <div class="head"></div>
        <div class="head">Average Qty<br>per Serving</div>
        <div class="head">Average Qty<br>per 100g</div>
        <div class="values">Energy<br>Protein<br>Fat, total<br>&nbsp;- saturated<br>Carbohydrate<br>&nbsp;- sugars<br>Sodium</div>
        <div class="values">272kJ<br>0.08g<br>0g<br>0g<br>15.9g<br>15.6g<br>2.4mg</div>
        <div class="values">1360kJ<br>0.38g<br>0g<br>0g<br>79.6g<br>78.1g<br>12mg</div>
      </div>
    </div>
  </div>

  <div class="back-footer">
    <div class="mini-brand">
      <span class="brand-dot"></span>
      CORVALE<br>FARMS
    </div>
    <div class="mini-title">
      CERTIFIED ORGANIC<br>PURE
      <p class="mini-script">Maple Syrup</p>
    </div>
    <div class="contact">
      <span class="contact-icon"></span>
      <p>14 Sugarbush Road, Northfield 12345, hello@corvalefarms.com</p>
    </div>
  </div>

  <div class="maple-leaf maple-leaf--bottom" role="img" aria-label="Gold maple leaf ornament"></div>
</section>

</body>
</html>
```